New Wine Label - Argentinian Malbec 'Viento Callado'

I am looking for an exceptional and exciting design for a wine label called 'Viento Callado' meaning Quiet Wind or Wind of the Quiet. The design must feature the name 'Viento Callado', a star logo and the word 'Malbec'. It will also need the words 'Mendoza, Argentina' at the bottom of the label as a prominent piece of information. Please produce the work in size 80mm x 100mm. Feel free to use colour in addition to black/white and ensue that the label is easy to read on a shelf placement.

Target Market(s)

25-50 Year Olds who enjoy great wine that looks and appears interesting and a little different.

Requirements
Must have
• Star Logo
• Word - Malbec
• Words - Mendoza, Argentina
Nice to have
• Background image to label

```html
<!DOCTYPE html>
<html lang="en">
<head>
<meta charset="utf-8">
<title>Viento Callado Malbec Label</title>
<link href="https://fonts.googleapis.com/css2?family=Oswald:wght@600&family=Roboto+Condensed:wght@700&family=Libre+Baskerville:ital@1&display=swap" rel="stylesheet">
<style>
  :root {
    --backdrop: #d3d2cd;
    --label: #f0eff0;
    --ink: #2b2827;
    --gold: #c9a646;
    --gold-light: #e6cf7d;
    --wine: #8e2a3f;
    --rule: #dcdadb;
  }
  html, body {
    margin: 0;
    padding: 0;
    width: 1200px;
    height: 1200px;
    overflow: hidden;
    background: var(--backdrop);
  }
  .label {
    position: absolute;
    left: 229px;
    top: 228px;
    width: 741px;
    height: 710px;
    background: var(--label);
    border-radius: 6px;
  }
  .brand-mark {
    position: absolute;
    left: 0;
    width: 100%;
    top: 214px;
    display: flex;
    align-items: center;
    justify-content: center;
    gap: 10px;
    font-family: "Oswald", sans-serif;
    font-weight: 600;
    font-size: 15px;
    letter-spacing: 3px;
    text-transform: uppercase;
    color: var(--gold);
  }
  .brand-mark .dot {
    width: 12px;
    height: 12px;
    border-radius: 50%;
    background: var(--gold);
  }
  .wine-name {
    position: absolute;
    left: 0;
    width: 100%;
    top: 372px;
    margin: 0;
    text-align: center;
    font-family: "Oswald", sans-serif;
    font-weight: 600;
    font-size: 68px;
    line-height: 67px;
    letter-spacing: 0.5px;
    color: var(--ink);
    text-transform: uppercase;
  }
  .details {
    position: absolute;
    right: 359px;
    top: 526px;
    text-align: right;
  }
  .varietal {
    font-family: "Roboto Condensed", sans-serif;
    font-weight: 700;
    font-size: 25px;
    letter-spacing: 2px;
    color: var(--ink);
    line-height: 30px;
  }
  .region, .role {
    font-family: "Libre Baskerville", serif;
    font-style: italic;
    font-size: 15px;
    letter-spacing: 1.5px;
    color: var(--ink);
  }
  .region { line-height: 26px; margin-top: -2px; }
  .vintage {
    font-family: "Roboto Condensed", sans-serif;
    font-weight: 700;
    font-size: 15px;
    letter-spacing: 2px;
    color: var(--ink);
    margin-top: 2px;
  }
  .vintage .year-end { color: var(--wine); font-size: 17px; }
  .divider {
    position: absolute;
    left: 400px;
    top: 524px;
    width: 1px;
    height: 90px;
    background: var(--rule);
  }
  .signature {
    position: absolute;
    left: 412px;
    top: 530px;
    width: 128px;
    height: 30px;
    border-radius: 3px;
    background: linear-gradient(90deg, var(--gold-light), var(--gold));
    opacity: 0.75;
  }
  .role {
    position: absolute;
    left: 416px;
    top: 560px;
  }
</style>
</head>
<body>
  <main class="label">
    <div class="brand-mark"><span class="dot"></span><span>Viento Callado</span></div>
    <h1 class="wine-name">Viento<br>Callado</h1>
    <div class="details">
      <div class="varietal">Malbec</div>
      <div class="region">Mendoza, Argentina</div>
      <div class="vintage">20<span class="year-end">12</span></div>
    </div>
    <div class="divider"></div>
    <div class="signature" role="img" aria-label="Winemaker's handwritten signature in gold foil"></div>
    <div class="role">Winemaker</div>
  </main>
</body>
</html>
```